PawQuarry Banner contest an ecommerce site for veterinarians

We need banners for our ecommerce site. Our site is a webstore that veterinarians can use to allow their clients to purchase items from them. Each month we have a different theme for our banners. I am looking for banners for January and February and with a refresh coming to our site could be looking at a dozen over the next year. I may potentially choose from multiple designers and increase the payment or will choose one designer for both months .

For January our theme is winter fun. We will be running a contest were people can submit a picture of their pet to our Chatterloop page enjoying the snow or keeping warm. they have a chance to win one of 5 $50 gift certificates to pawquarry. The banner should have a dog and cat and a separate one with just a cat. We will need a French and English banner. We will provide the French translation once the winner has been selected.

For February our theme is dental health. The banner should have a dog and cat and a separate one with just a cat. We will need a French and English banner. We will provide the French translation once the winner has been selected.

Target Market(s)

pet owners

Industry/Entity Type

Veterinary

Colors

Designer to choose colors to be used in the design.

Requirements
Must have
• dimensions for PQ Banner are: 710px x 280px
Nice to have
• I have attached our logo and some screen shoots of our site so you can get a feel of what it look like. you could also go to www.pawquarry.ca and see what the sign in page looks like
Should not have
• images of pet food

```html
<!DOCTYPE html>
<html lang="en">
<head>
<meta charset="utf-8">
<title>PawQuarry – Winter Fun Contest Banner</title>
<link rel="stylesheet" href="https://fonts.googleapis.com/css2?family=Open+Sans:wght@400;600;700&display=swap">
<style>
  :root {
    --snow-light: #eef2f6;
    --snow-mid: #c9d3de;
    --snow-shadow: #8e9bab;
    --tree-dark: #4a5664;
    --pet-warm: #b79a7e;
    --pet-blanket: #cfcac4;
    --headline-white: #ffffff;
    --brand-blue: #2d67ad;
    --panel-white: rgba(255, 255, 255, 0.88);
    --panel-ring: rgba(255, 255, 255, 0.4);
    --prize-band: #b3c9e4;
  }

  html, body {
    margin: 0;
    padding: 0;
    overflow: hidden;
    background: #ffffff;
  }

  .banner {
    position: relative;
    width: 1200px;
    height: 473px;
    overflow: hidden;
    font-family: "Open Sans", Arial, sans-serif;
  }

  .winter-scene {
    position: absolute;
    inset: 0;
    background:
      radial-gradient(ellipse at 78% 8%, var(--tree-dark) 0%, rgba(74, 86, 100, 0) 45%),
      linear-gradient(180deg, var(--snow-mid) 0%, var(--snow-light) 55%, var(--snow-mid) 100%);
  }

  .pets-blanket {
    position: absolute;
    left: 690px;
    top: 40px;
    width: 510px;
    height: 433px;
    border-radius: 40% 0 0 0;
    background: linear-gradient(160deg, var(--pet-warm) 0%, var(--pet-blanket) 55%, var(--snow-shadow) 100%);
  }

  .headline {
    position: absolute;
    left: 57px;
    top: 36px;
    margin: 0;
    font-size: 34px;
    font-weight: 700;
    color: var(--headline-white);
    text-shadow: 0 1px 3px rgba(60, 80, 100, 0.45);
  }

  .subheadline {
    position: absolute;
    left: 57px;
    top: 104px;
    margin: 0;
    font-size: 33px;
    line-height: 47px;
    font-weight: 600;
    color: var(--brand-blue);
  }

  .contest-panel {
    position: absolute;
    left: 176px;
    top: 215px;
    width: 510px;
    height: 510px;
    border-radius: 50%;
    background: var(--panel-white);
    box-shadow: 0 0 0 16px var(--panel-ring);
    overflow: hidden;
  }

  .prize-band {
    position: absolute;
    left: 0;
    right: 0;
    top: 170px;
    height: 58px;
    background: var(--prize-band);
  }

  .contest-copy {
    position: absolute;
    left: 231px;
    width: 400px;
    top: 252px;
    text-align: center;
    color: var(--brand-blue);
  }

  .contest-copy p {
    margin: 0;
  }

  .contest-invite {
    font-size: 20px;
    line-height: 29px;
  }

  .contest-chance {
    margin-top: 8px !important;
    font-size: 24px;
    font-weight: 600;
  }

  .prize {
    position: absolute;
    left: 231px;
    width: 400px;
    top: 388px;
    margin: 0;
    text-align: center;
    font-size: 26px;
    color: var(--brand-blue);
  }

  .prize-amount {
    font-size: 36px;
    font-weight: 700;
  }

  .prize-currency {
    font-size: 24px;
    font-weight: 700;
  }
</style>
</head>
<body>
  <div class="banner">
    <div class="winter-scene" role="img" aria-label="Snowy park with frosted trees and a snow-covered bench"></div>
    <div class="pets-blanket" role="img" aria-label="A tabby cat and a small terrier dog wrapped together in a grey checked blanket"></div>

    <h1 class="headline">Winter is more cooler with your Pets!</h1>
    <h2 class="subheadline">Are they enjoying the snow<br>or keeping warm?</h2>

    <div class="contest-panel">
      <div class="prize-band"></div>
    </div>

    <div class="contest-copy">
      <p class="contest-invite">Share a picture<br>of your pet having fun<br>in winter to our Chatterloop page.</p>
      <p class="contest-chance">They have a chance to win</p>
    </div>

    <p class="prize"><span class="prize-currency">$</span><span class="prize-amount">50</span> gift certificates</p>
  </div>
</body>
</html>
```